metal roofing website

I have several domain names and a website that has been built. I need someone to recreate essentially the same website and change some photos and basic design to create the new sites. I have all of the files and c panel access to the lucky winner. If you can do a good job at a fair price I will have 100's of sites to send to you very soon. I have the site built and have all files just need it recreated on my server. the current site is www.brantlepanelinc.com I am looking to get this done ASAP!!!

```html
<!DOCTYPE html>
<html lang="en">
<head>
<meta charset="utf-8">
<title>Brantle Panel – Metal Building Components</title>
<link href="https://fonts.googleapis.com/css2?family=Montserrat:wght@500;600;700&family=Open+Sans:wght@400;600;700&display=swap" rel="stylesheet">
<style>
:root{
  --red:#c4161c;
  --red-dark:#9e0f14;
  --tan:#e6d3c0;
  --tan-line:#d4bca5;
  --dark:#1c1c1e;
  --ink:#2a2a2a;
  --white:#ffffff;
  --muted:#555;
}
*{margin:0;padding:0;box-sizing:border-box}
html,body{width:1200px;height:3947px;overflow:hidden}
body{position:relative;background:var(--tan);font-family:"Open Sans",sans-serif;color:var(--ink)}
.abs{position:absolute}
.heading{font-family:"Montserrat",sans-serif;font-weight:600}

/* top bar */
.topbar{left:0;top:0;width:1200px;height:40px;border-bottom:2px solid var(--tan-line);font-size:13px}
.topbar .socials{left:112px;top:13px;display:flex;gap:12px}
.topbar .socials span{width:13px;height:13px;border-radius:50%;background:var(--red)}
.topbar .contact{right:112px;top:0;height:40px;display:flex;align-items:center;gap:28px;padding-left:14px;border-left:1px solid var(--tan-line)}
.topbar .contact b{color:var(--red);font-weight:600}

/* nav */
.brand{left:112px;top:66px;font-family:"Montserrat",sans-serif;font-weight:700;font-size:26px;color:var(--red);letter-spacing:1px;display:flex;align-items:center;gap:10px}
.brand i{width:22px;height:22px;background:var(--red);display:block}
.nav{left:465px;top:82px;display:flex;gap:36px;font-size:18px;color:var(--ink)}
.nav .active{color:var(--red)}

/* hero */
.hero{left:0;top:152px;width:1200px;height:600px}

/* about */
.about-frame{left:80px;top:864px;width:195px;height:120px;border-top:3px dashed var(--red-dark);border-left:3px dashed var(--red-dark)}
.about-dots{left:385px;top:1050px;width:175px;height:150px;background-image:radial-gradient(var(--red-dark) 1.3px,transparent 1.6px);background-size:7px 7px;opacity:.7}
.about-img{left:97px;top:884px;width:448px;height:306px;background:linear-gradient(160deg,#6f8a4a 0%,#7a3f5a 35%,#d9c48a 65%,#4f6b35 100%)}
.about-title{left:584px;top:888px;font-size:38px;color:var(--red);font-weight:500}
.about-sub{left:584px;top:940px;font-size:16px;font-weight:700;font-family:"Montserrat",sans-serif}
.about-text{left:584px;top:968px;width:540px;font-size:14.5px;line-height:31px;text-align:justify}
.btn{background:var(--red);color:var(--white);font-weight:700;font-family:"Montserrat",sans-serif;display:flex;align-items:center;justify-content:center;gap:10px}
.about-btn{left:584px;top:1147px;width:198px;height:53px;border-radius:27px;font-size:17px}

/* offer */
.offer-title{left:0;width:1200px;top:1440px;text-align:center;color:var(--white);font-size:40px;letter-spacing:1px}
.offer-lead{left:220px;width:760px;top:1502px;text-align:center;color:#ddd;font-size:15px;line-height:31px}
.history{left:97px;top:1618px;width:319px;height:566px;background:var(--white)}
.history-img{left:27px;top:27px;width:271px;height:258px;background:linear-gradient(180deg,#c9ccd1 0%,#9ba1a8 45%,#7f7768 70%,#5e5545 100%)}
.history h3{position:absolute;left:27px;top:308px;color:var(--red);font-size:21px;font-weight:500;font-family:"Montserrat",sans-serif}
.history p{position:absolute;left:27px;top:342px;width:268px;font-size:12.5px;line-height:24px;text-align:justify;color:var(--muted)}
.history .btn{position:absolute;left:0;bottom:0;width:319px;height:46px;font-size:16px}
.card{width:307px;height:222px;background:var(--white);text-align:center}
.card .icon{position:absolute;left:115px;top:-38px;width:77px;height:77px;border-radius:50%;background:var(--white);border:2px solid #eee;display:flex;align-items:center;justify-content:center}
.card h4{position:absolute;left:10px;right:10px;top:56px;color:var(--red);font-size:17px;font-weight:600;line-height:22px;font-family:"Montserrat",sans-serif}
.card p{position:absolute;left:20px;right:20px;top:104px;font-size:12.5px;line-height:22px;color:var(--muted)}
.card .more{position:absolute;left:0;right:0;top:186px;color:var(--red);font-size:14px;font-weight:700}

/* gallery */
.gallery-title{left:0;width:1200px;top:2316px;text-align:center;color:var(--red);font-size:33px}
.tile{width:316px;height:204px}

/* contact */
.info-icon{width:84px;height:84px;border-radius:50%;background:var(--red);display:flex;align-items:center;justify-content:center}
.info-text{color:var(--white);font-size:17px;line-height:29px;text-align:center;width:340px}
.field{height:40px;background:var(--white);font-size:13px;color:#666;padding-left:16px;display:flex;align-items:center;gap:8px}
.field.area{align-items:flex-start;padding-top:12px}
.submit{left:511px;top:3464px;width:179px;height:36px;font-size:16px}

/* footer */
.foot-brand{left:0;width:1200px;top:3700px;justify-content:center}
.foot-socials{left:0;width:1200px;top:3800px;display:flex;justify-content:center;gap:12px}
.foot-socials span{width:42px;height:42px;border-radius:50%;border:3px solid var(--red);display:block}
.foot-nav{left:0;width:1200px;top:3866px;text-align:center;font-size:17px}
.foot-nav span{margin:0 12px}
.copy{left:0;width:1200px;top:3906px;text-align:center;font-size:13px}
</style>
</head>
<body>

<!-- top bar -->
<div class="abs topbar">
  <div class="abs socials"><span></span><span></span><span></span><span></span><span></span><span></span><span></span></div>
  <div class="abs contact">
    <div><b>✉ Email us:</b> info@brantlepanelinc.com</div>
    <div><b>✆ Call us:</b> 555-201-0765</div>
  </div>
</div>

<!-- header -->
<div class="abs brand"><i></i>BRANTLE PANEL</div>
<nav class="abs nav">
  <span class="active">Home</span><span>About Us</span><span>Services</span><span>Gallery</span><span>Contact Us</span><span>Get a Quote</span>
</nav>

<!-- hero -->
<svg class="abs hero" width="1200" height="600" viewBox="0 0 1200 600">
  <defs>
    <linearGradient id="heroSky" x1="0" y1="0" x2="0" y2="1">
      <stop offset="0" stop-color="#bfc4c6"/><stop offset=".45" stop-color="#d6d7d0"/>
      <stop offset=".62" stop-color="#8f8a7a"/><stop offset=".78" stop-color="#4c7a2e"/><stop offset="1" stop-color="#3f6a26"/>
    </linearGradient>
  </defs>
  <polygon points="0,470 600,568 1200,470 1200,490 600,590 0,490" fill="var(--red)"/>
  <polygon points="0,0 1200,0 1200,470 600,568 0,470" fill="url(#heroSky)" role="img" aria-label="Photo of a large metal pole building with wraparound porch on a green lawn"/>
</svg>

<!-- about -->
<div class="abs about-frame"></div>
<div class="abs about-dots"></div>
<div class="abs about-img" role="img" aria-label="Photo of a two-storey house with a purple metal roof"></div>
<h2 class="abs about-title heading">ABOUT US</h2>
<div class="abs about-sub">MANUFACTURERS OF QUALITY BUILDING COMPONENTS</div>
<p class="abs about-text">Sed ut perspiciatis unde omnis iste natus error sit voluptatem accusantium doloremque laudantium, totam rem aperiam, eaque ipsa quae ab illo inventore veritatis et quasi architecto beatae vitae dicta sunt explicabo. Nemo enim ipsam voluptatem quia voluptas sit aspernatur aut odit aut fugit, sed quia consequuntur magni dolores eos qui ratione voluptatem sequi nesciunt.</p>
<div class="abs btn about-btn">▶ Read More</div>

<!-- what we offer -->
<svg class="abs" style="left:0;top:1310px" width="1200" height="945" viewBox="0 0 1200 945">
  <polygon points="0,75 600,0 1200,75 1200,945 0,945" fill="var(--red)"/>
  <polygon points="0,85 600,14 1200,85 1200,945 0,945" fill="var(--dark)" role="img" aria-label="Darkened photo backdrop of a farm building at dusk"/>
</svg>
<h2 class="abs offer-title heading">WHAT WE OFFER</h2>
<p class="abs offer-lead">Aenean sollicitudin, lorem quis bibendum auctor, nisi elit consequat ipsum,sem nibh id elit. Duis sed odio sit amet nibh vulputate cursus a sit amet mauris. Morbi accumsan ipsum velit</p>

<div class="abs history">
  <div class="abs history-img" role="img" aria-label="Photo of a grey steel storage building with red trim"></div>
  <h3>COMPANY HISTORY</h3>
  <p>Sed ut perspiciatis unde omnis iste natus error sit voluptatem accusantium doloremque laudantium, totam rem aperiam, eaque ipsa quae ab illo inventore veritatis et quasi architecto beatae vitae dicta sunt explicabo nemo enim ipsam voluptatem.</p>
  <div class="btn">⬇ Download PDF</div>
</div>

<div class="abs card" style="left:461px;top:1668px">
  <div class="icon"><svg width="40" height="40" viewBox="0 0 40 40" fill="none" stroke="var(--red)" stroke-width="2"><rect x="4" y="12" width="20" height="14"/><path d="M24 16h7l5 5v5H24z"/><circle cx="11" cy="29" r="3"/><circle cx="30" cy="29" r="3"/></svg></div>
  <h4>We can deliver</h4>
  <p>This is a sample version of Lorem Ipsum. Proin gravida nibh vel velit auctor aliquet. Aenean lorem quis bibendum lorem quis</p>
  <div class="more">Read More ➔</div>
</div>
<div class="abs card" style="left:795px;top:1668px">
  <div class="icon"><svg width="40" height="40" viewBox="0 0 40 40" fill="none" stroke="var(--red)" stroke-width="2"><path d="M5 35V16L20 5l15 11v19z"/><path d="M12 35V22h16v13"/><path d="M12 28h16"/></svg></div>
  <h4>Complete Post frame building Packages</h4>
  <p>This is a sample version of Lorem Ipsum. Proin gravida nibh vel velit auctor aliquet. Aenean lorem quis bibendum lorem quis</p>
  <div class="more">Read More ➔</div>
</div>
<div class="abs card" style="left:461px;top:1963px">
  <div class="icon"><svg width="40" height="40" viewBox="0 0 40 40" fill="none" stroke="var(--red)" stroke-width="2"><path d="M3 20L20 6l17 14"/><path d="M8 17v18h24V17"/><rect x="16" y="24" width="8" height="11"/></svg></div>
  <h4>Residential Metal Roofing</h4>
  <p>This is a sample version of Lorem Ipsum. Proin gravida nibh vel velit auctor aliquet. Aenean lorem quis bibendum lorem quis</p>
  <div class="more">Read More ➔</div>
</div>
<div class="abs card" style="left:795px;top:1963px">
  <div class="icon"><svg width="40" height="40" viewBox="0 0 40 40" fill="none" stroke="var(--red)" stroke-width="2"><rect x="6" y="6" width="28" height="29"/><path d="M6 13h28M11 19h6M23 19h6M11 25h6M23 25h6M17 35v-6h6v6"/></svg></div>
  <h4>Commercial Applications</h4>
  <p>This is a sample version of Lorem Ipsum. Proin gravida nibh vel velit auctor aliquet. Aenean lorem quis bibendum lorem quis</p>
  <div class="more">Read More ➔</div>
</div>

<!-- gallery -->
<h2 class="abs gallery-title heading">OUR GALLERY</h2>
<div class="abs tile" style="left:116px;top:2408px;background:linear-gradient(180deg,#c5ccd4 0%,#9a9e9e 45%,#5f7d3a 70%,#4d6e2e 100%)" role="img" aria-label="Photo of a commercial metal building complex with lawn"></div>
<div class="abs tile" style="left:442px;top:2408px;background:linear-gradient(180deg,#3c7fc4 0%,#8fa7bd 40%,#5b6470 70%,#6e6251 100%)" role="img" aria-label="Photo of a grey metal pole barn under a blue sky"></div>
<div class="abs tile" style="left:768px;top:2408px;background:linear-gradient(180deg,#aeb6bf 0%,#7a2a2a 40%,#8c3030 65%,#5e6f3a 100%)" role="img" aria-label="Photo of a red barn with white trim"></div>
<div class="abs tile" style="left:116px;top:2621px;background:linear-gradient(180deg,#4b8ad0 0%,#a7b9c9 35%,#b59d7e 60%,#6b5845 100%)" role="img" aria-label="Photo of a tan metal garage building with overhead doors"></div>
<div class="abs tile" style="left:442px;top:2621px;background:linear-gradient(180deg,#8fb1d6 0%,#6a3d55 40%,#cbb88a 70%,#4e6a33 100%)" role="img" aria-label="Photo of a brick house with a purple metal roof"></div>
<div class="abs tile" style="left:768px;top:2621px;background:linear-gradient(160deg,#6f8a4a 0%,#7a3f5a 35%,#d9c48a 65%,#4f6b35 100%)" role="img" aria-label="Photo of a two-storey house with a purple metal roof"></div>

<!-- contact -->
<svg class="abs" style="left:0;top:2900px" width="1200" height="775" viewBox="0 0 1200 775">
  <polygon points="0,8 1200,8 1200,680 600,765 0,680" fill="var(--dark)" role="img" aria-label="Darkened photo backdrop of a barn with a round metal roof"/>
  <polygon points="0,8 600,88 1200,8 1200,0 0,0" fill="var(--tan)"/>
  <polyline points="0,8 600,88 1200,8" fill="none" stroke="var(--red)" stroke-width="8"/>
  <polyline points="0,680 600,765 1200,680" fill="none" stroke="var(--red)" stroke-width="8"/>
</svg>
<div class="abs info-icon" style="left:274px;top:3071px"><svg width="40" height="40" viewBox="0 0 40 40" fill="none" stroke="#fff" stroke-width="2.5"><path d="M20 36S8 23 8 15a12 12 0 0124 0c0 8-12 21-12 21z"/><circle cx="20" cy="15" r="4"/></svg></div>
<div class="abs info-icon" style="left:558px;top:3071px"><svg width="40" height="40" viewBox="0 0 40 40" fill="none" stroke="#fff" stroke-width="2.5"><path d="M9 5h7l3 8-4 3a20 20 0 009 9l3-4 8 3v7c0 2-2 3-4 3C18 34 6 22 6 9c0-2 1-4 3-4z"/></svg></div>
<div class="abs info-icon" style="left:855px;top:3071px"><svg width="40" height="40" viewBox="0 0 40 40" fill="none" stroke="#fff" stroke-width="2.5"><rect x="5" y="9" width="30" height="22"/><path d="M5 9l15 13 15-13"/></svg></div>
<div class="abs info-text" style="left:146px;top:3165px">48 Ridge Line Rd Ste 12, Fairmont<br>NX, 48120</div>
<div class="abs info-text" style="left:430px;top:3165px">Phone: 555-201-0765<br>Fax: 555-201-0994</div>
<div class="abs info-text" style="left:727px;top:3165px">Email: info@company.com<br>Support: support@company.com</div>

<div class="abs field" style="left:163px;top:3245px;width:427px">👤 First Name</div>
<div class="abs field" style="left:611px;top:3245px;width:426px">👤 Last Name</div>
<div class="abs field" style="left:163px;top:3300px;width:427px">▦ Address</div>
<div class="abs field" style="left:163px;top:3353px;width:427px">✉ Email Address</div>
<div class="abs field" style="left:163px;top:3408px;width:427px">✆ Phone Number</div>
<div class="abs field area" style="left:611px;top:3300px;width:426px;height:147px">✎ Message :</div>
<div class="abs btn submit">➤ Submit</div>

<!-- footer -->
<div class="abs brand foot-brand"><i></i>BRANTLE PANEL</div>
<div class="abs foot-socials"><span></span><span></span><span></span><span></span></div>
<div class="abs foot-nav">Home <span>|</span> About us <span>|</span> Our Services <span>|</span> Gallery <span>|</span> Contact</div>
<div class="abs copy">Copyrights © 2015. All Rights Reserved</div>

</body>
</html>
```